WEBSITE: Security Officer Training, Security Officer Certifications, Security Officer Job Training

colorful and simple website, NO FLASH, and easy for SEO
Able to Upload to GODADDY WEBSITE BUILDER!

We need a great image that depicts and sell Harborline Watch Academy
Our websites for info: Security Officers doing cool things, the pictures must be great..

FEEL Free to choose ideas from our services in our
Www.harborlinewatchacademy.org site
The CPO certified protection officer tab
The CFO certified Firearms Office tab
The Security Officer Academy
The Campus security officer
Will be a few pages, landing page and contact page..
Www.harborlinewatchacademy.org
Www.civicwardenhall.net
Www.patrolcredentialhub.com
ALSO go to goggle and put in
Los Angles "Security Guard Training"
California Guard Card
Guard Card
Firearms Training
And similar words to see competitors websites!

WE want our more KICK ASS and COOOL!

OUr Industry: Security Officer Training Certifications
INFO: SECURITY OFFICER TRAINING
Law Enforcement
Police
Criminal Justice Training
Security Guards
Security Professional

Target Market(s)

Law Enforcement Training
Police Training
Criminal Justice Training
Security Officer Training
Security Officer Certifications

Industry/Entity Type

Security

Number of Pages Required

3 page

Requirements
Must have
• Able to upload to GODADDY WEBSITE BUILDER
• Easy to edit
• Must be easy for SEO
• NO FLASH or other things that prevent mobile phones
• MOBILE PHONE COMPATIBLE
• COOL!
• Call to action
• Contact form for email sign ups
• PICTURES SLIDE SHOW MUST HAVE
Should not have
• NO have flash

```html
<!DOCTYPE html>
<html lang="en">
<head>
<meta charset="utf-8">
<title>Harborline Watch Academy</title>
<link href="https://fonts.googleapis.com/css2?family=Oswald:wght@400;500&family=Arvo:wght@700&family=Lato:wght@400;700&display=swap" rel="stylesheet">
<style>
:root{
  --gold:#f5e0a0;
  --gold-line:#e8c25a;
  --navy:#1f1660;
  --navy-deep:#1b1456;
  --ink:#1a1a1a;
  --text:#333;
  --muted:#777;
  --black:#0b0b0b;
  --white:#fff;
  --frame:#b9a46c;
}
*{margin:0;padding:0;box-sizing:border-box}
html,body{width:1200px;height:2628px;overflow:hidden}
body{font-family:"Lato",sans-serif;color:var(--text);background:var(--white);position:relative}
.heading{font-family:"Oswald",sans-serif;font-weight:400;text-transform:uppercase}
.btn{display:inline-block;background:var(--gold);color:var(--ink);font-family:"Oswald",sans-serif;text-transform:uppercase;border-radius:3px;text-decoration:none}
.rule{height:3px;background:var(--gold-line)}

/* navigation */
.topbar{position:absolute;top:0;left:0;width:1200px;height:44px;background:var(--black);display:flex;justify-content:flex-end;align-items:stretch;padding-right:50px}
.topbar a{font-family:"Oswald",sans-serif;color:var(--white);text-decoration:none;font-size:17px;padding:0 20px;display:flex;align-items:center;text-transform:uppercase}
.topbar a.active{background:#c9ab5f}
.topbar .call{color:var(--gold);border-left:1px solid #555;margin-left:8px;padding-left:18px}

/* hero */
.hero{position:absolute;top:44px;left:0;width:1200px;height:596px;background:radial-gradient(ellipse at 40% 40%,#6f6f6a 0%,#4d4e4a 45%,#2c2c2b 100%)}
.hero .photo{position:absolute;inset:0}
.brand{position:absolute;top:10px;left:72px;width:166px;height:200px;border-radius:50%;background:var(--black);display:flex;align-items:center;justify-content:center;text-align:center;font-family:"Oswald",sans-serif;color:var(--gold);font-size:20px;line-height:1.25;padding:18px;z-index:2}
.hero-copy{position:absolute;top:212px;left:540px;width:580px;text-align:center}
.hero-copy h1{font-family:"Arvo",serif;color:var(--white);font-size:29px;line-height:48px;letter-spacing:1px;text-transform:uppercase}
.hero-copy .btn{margin-top:26px;font-size:24px;padding:4px 22px}
.arrow{position:absolute;top:280px}

/* welcome */
.welcome{position:absolute;top:640px;left:0;width:1200px;height:311px;text-align:center}
.welcome h2{margin-top:42px;font-size:25px;color:var(--ink)}
.welcome h2 span{color:var(--navy)}
.welcome .rule{width:118px;margin:18px auto 0}
.welcome p{width:1020px;margin:30px auto 0;font-size:14.5px;line-height:24px;color:var(--ink)}
.welcome .btn{margin-top:25px;font-size:16px;padding:5px 15px}

/* certifications */
.certs{position:absolute;top:951px;left:0;width:1200px;height:640px;background:linear-gradient(180deg,#3c3d3a,#2a2b29 60%,#363633)}
.certs h2{position:absolute;top:38px;width:100%;text-align:center;color:var(--white);font-size:34px}
.certs .line{position:absolute;top:108px;left:290px;width:620px;height:1px;background:rgba(255,255,255,.35)}
.certs .line i{position:absolute;left:270px;top:-1px;width:80px;height:3px;background:var(--gold-line)}
.tile{position:absolute;width:324px;height:193px;border:9px solid var(--frame);display:flex;align-items:center;justify-content:center}
.tile span{position:relative;font-family:"Oswald",sans-serif;color:var(--white);font-size:23px;text-transform:uppercase;text-shadow:0 1px 3px rgba(0,0,0,.7)}

/* courses + blog */
.split{position:absolute;top:1591px;left:0;width:1200px;height:461px}
.courses{position:absolute;left:82px;top:0;width:605px}
.section-title{font-size:35px;color:var(--ink);margin-top:36px}
.section-title span{color:var(--navy)}
.courses .view{position:absolute;right:0;top:58px;font-family:"Oswald",sans-serif;font-size:14px;color:var(--navy)}
.title-rule{position:relative;height:1px;background:#ddd;margin-top:14px}
.title-rule i{position:absolute;left:0;top:-1px;width:86px;height:3px;background:var(--gold-line)}
.course{position:absolute;top:137px;width:280px;text-align:center}
.course .thumb{width:280px;height:154px;border:3px solid #e5e5e5}
.course h3{margin-top:14px;font-family:"Oswald",sans-serif;font-weight:400;font-size:17px;color:var(--navy);text-transform:uppercase}
.course .price{margin-top:6px;font-family:"Oswald",sans-serif;font-size:24px;color:var(--ink)}
.course .price small{font-size:16px;text-transform:uppercase}
.course .btn{margin-top:8px;font-size:16px;padding:4px 15px}
.blog{position:absolute;left:752px;top:0;width:366px}
.post{margin-top:24px}
.post+.post{border-top:1px solid #e5e5e5;padding-top:22px}
.post h3{font-family:"Oswald",sans-serif;font-weight:400;font-size:17px;color:var(--navy)}
.post time{display:block;font-size:12px;color:var(--muted);margin-top:8px}
.post p{font-size:13px;line-height:20px;color:var(--ink);margin-top:8px}
.post p em{color:var(--gold-line);font-style:normal}

/* free training */
.free{position:absolute;top:2052px;left:0;width:1200px;height:285px;background:var(--gold);text-align:center}
.free h2{margin-top:34px;font-size:36px;color:var(--ink)}
.free h2 span{color:var(--navy)}
.free .rule{width:360px;height:1px;background:rgba(255,255,255,.7);margin:12px auto 0;position:relative}
.free .rule i{position:absolute;left:140px;top:-1px;width:80px;height:3px;background:var(--navy)}
.free p{width:1000px;margin:24px auto 0;font-size:21px;line-height:38px;color:var(--ink)}
.free .btn{margin-top:22px;background:var(--navy);color:var(--white);font-size:17px;padding:5px 18px}

/* footer */
.footer{position:absolute;top:2337px;left:0;width:1200px;height:246px;background:var(--navy-deep);color:var(--white)}
.col{position:absolute;top:40px}
.col h4{font-family:"Oswald",sans-serif;font-weight:400;font-size:18px;text-transform:uppercase}
.col .u{width:120px;height:1px;background:rgba(255,255,255,.4);margin-top:12px;position:relative}
.col .u i{position:absolute;left:0;top:-1px;width:46px;height:3px;background:var(--gold-line)}
.col ul{list-style:none;margin-top:24px}
.col li{font-size:12px;line-height:24px}
.col li::before{content:"›";margin-right:9px}
.divider{position:absolute;top:30px;width:1px;height:180px;background:rgba(255,255,255,.15)}
.contact-row{display:flex;gap:14px;font-size:12px;line-height:16px;margin-top:18px}
.contact-row svg{flex:none;margin-top:2px}
.map{margin-top:24px;width:210px;height:116px;background:linear-gradient(135deg,#e6e1d3,#cfd9c4 60%,#b9cbe0)}
.social{list-style:none;margin-top:20px}
.social li{display:flex;align-items:center;gap:10px;font-size:12px;line-height:30px}
.social li::before{content:none}
.social b{display:block;width:20px;height:20px;background:var(--white)}
.copyright{position:absolute;top:2583px;left:0;width:1200px;height:45px;background:var(--gold);text-align:center;font-size:13px;line-height:45px;color:var(--ink)}
</style>
</head>
<body>

<nav class="topbar">
  <a class="active" href="#">Home</a>
  <a href="#">About Us</a>
  <a href="#">Courses</a>
  <a href="#">Blog</a>
  <a href="#">Contact Us</a>
  <a class="call" href="#">Call us today (123) 456-7890</a>
</nav>

<header class="hero">
  <div class="photo" role="img" aria-label="Slideshow photo: trainee aiming a handgun at a firing range target"></div>
  <div class="brand">Harborline Watch Academy</div>
  <svg class="arrow" style="left:26px" width="16" height="34" viewBox="0 0 16 34"><polyline points="14,2 2,17 14,32" fill="none" stroke="#fff" stroke-width="2"/></svg>
  <svg class="arrow" style="right:26px" width="16" height="34" viewBox="0 0 16 34"><polyline points="2,2 14,17 2,32" fill="none" stroke="#fff" stroke-width="2"/></svg>
  <div class="hero-copy">
    <h1>Skills training course for the<br>certified protection officer</h1>
    <a class="btn" href="#">Join Now</a>
  </div>
</header>

<section class="welcome">
  <h2 class="heading">Welcome to <span>Harborline Watch Academy</span></h2>
  <div class="rule"></div>
  <p>Lorem ipsum dolouar sit amet consec tetuer adipiscing elnit. Praebulum molesbeutie lacus. Aenea nonuendrerit maurihasellu porta. Fusce suscpvarius mi. Cum sociis natoque penatibus et magnis dis parturientontes nascetur ridiculus mus. Nulla dui. Fusce feugiat mal esuada odio. Morbi nunc odio gravida atcursus necuctus a lorem. Lorem ipsum dolouar sit amet consec tetuer adipiscing elnit. Praebulum molesbeutie lacus.</p>
  <a class="btn" href="#">Read More</a>
</section>

<section class="certs" role="img" aria-label="Dimmed background photo of a training campus street">
  <h2 class="heading">We provide certifications for</h2>
  <div class="line"><i></i></div>
  <div class="tile" style="left:82px;top:153px;background:linear-gradient(135deg,#8a8b90,#4a4b50)" role="img" aria-label="Police badge and handcuffs"><span>Law Enforcement</span></div>
  <div class="tile" style="left:438px;top:153px;background:linear-gradient(135deg,#6f8a5a,#2f3a4a)" role="img" aria-label="Two police officers in uniform"><span>Police</span></div>
  <div class="tile" style="left:794px;top:153px;background:linear-gradient(135deg,#9a9a98,#3d3d3f)" role="img" aria-label="Trainees in a training hall"><span>Criminal Justice Training</span></div>
  <div class="tile" style="left:82px;top:391px;background:linear-gradient(135deg,#5d6a4e,#1e1f22)" role="img" aria-label="Security guard at a gate"><span>Security Guards</span></div>
  <div class="tile" style="left:438px;top:391px;background:linear-gradient(135deg,#55565a,#1d1d20)" role="img" aria-label="Security professional in white shirt and tie"><span>Security Professional</span></div>
  <div class="tile" style="left:794px;top:391px;background:linear-gradient(135deg,#3f6f9a,#1d2e44)" role="img" aria-label="Operator watching surveillance monitors"><span>All Type Security</span></div>
</section>

<section class="split">
  <div class="courses">
    <h2 class="heading section-title">Our Courses</h2>
    <a class="view" href="#">VIEW ALL</a>
    <div class="title-rule"><i></i></div>
    <div class="course" style="left:0">
      <div class="thumb" role="img" aria-label="Trainees practising restraint techniques outdoors" style="background:linear-gradient(135deg,#c9a98a,#2a2c34)"></div>
      <h3>Lorem ut perspiciatis unde iste mo</h3>
      <div class="price">$345 <small>per person</small></div>
      <a class="btn" href="#">Book Now</a>
    </div>
    <div class="course" style="left:319px">
      <div class="thumb" role="img" aria-label="Line of cadets kneeling during drills" style="background:linear-gradient(135deg,#8c8f95,#3a3f4c)"></div>
      <h3>Lorem ut perspiciatis unde iste mo</h3>
      <div class="price">$240 <small>per person</small></div>
      <a class="btn" href="#">Book Now</a>
    </div>
  </div>
  <div class="blog">
    <h2 class="heading section-title">Recent <span>Blog Posts</span></h2>
    <div class="title-rule"><i></i></div>
    <article class="post">
      <h3>Lorem ut perspiciatis unde iste mo dolor almet sit</h3>
      <time>11.July.2016</time>
      <p>Duis autem vel eum iriure dolor in hendrerit ink vulput dolor ateLorem ipsum dolor sit amet, consectetuer dolor adipiscing elit velit esse almet molestie facilisis. <em>[+]</em></p>
    </article>
    <article class="post">
      <h3>Lorem ut perspiciatis unde iste mo dolor almet sit</h3>
      <time>11.July.2016</time>
      <p>Lorem ipsum dolor sit amet, consectetuer adipiscing elit, sed diam nonummy nibh euismod tincidunt ut laoreet dolo magna aliquam erat volutpat wisi enim ad minim dolor veniam, quis nostrud ullamcorper . <em>[+]</em></p>
    </article>
  </div>
</section>

<section class="free">
  <h2 class="heading">Free <span>Training</span></h2>
  <div class="rule"><i></i></div>
  <p>Lorem ipsum dolouar sit amet consec tetuer adipiscing elnit. Praebulum molesbeutie lacus. Aenea nonuendrerit maurihasellu porta.</p>
  <a class="btn" href="#">Get Started</a>
</section>

<footer class="footer">
  <div class="col" style="left:82px">
    <h4>Quick Links</h4>
    <div class="u"><i></i></div>
    <ul><li>Home</li><li>About Us</li><li>Courses</li><li>Blog</li><li>Contact Us</li></ul>
  </div>
  <div class="divider" style="left:260px"></div>
  <div class="col" style="left:326px;width:230px">
    <h4>Contact Details</h4>
    <div class="u" style="width:230px"><i></i></div>
    <div class="contact-row" style="margin-top:22px">
      <svg width="10" height="14" viewBox="0 0 10 14"><path d="M5 0a5 5 0 0 0-5 5c0 4 5 9 5 9s5-5 5-9a5 5 0 0 0-5-5zm0 7a2 2 0 1 1 0-4 2 2 0 0 1 0 4z" fill="#fff"/></svg>
      <span>Lorem ipsum dolor sit consectetuer adipiscing elit,&nbsp; diam nonummy nibh Street No 5, zip Code: 897410</span>
    </div>
    <div class="contact-row">
      <svg width="12" height="12" viewBox="0 0 12 12"><path d="M2.5 0l2 3-1.2 1.3a7 7 0 0 0 4.4 4.4L9 7.5l3 2-1.5 2.5C5 12 0 7 0 1.5z" fill="#fff"/></svg>
      <span>012-345-6789</span>
    </div>
    <div class="contact-row">
      <svg width="12" height="9" viewBox="0 0 12 9"><rect width="12" height="9" fill="#fff"/><polyline points="0,0 6,5 12,0" fill="none" stroke="#1b1456" stroke-width="1.2"/></svg>
      <span>info@harborlinewatchacademy.org</span>
    </div>
  </div>
  <div class="divider" style="left:612px"></div>
  <div class="col" style="left:678px">
    <h4>Location Map</h4>
    <div class="u" style="width:210px"><i></i></div>
    <div class="map" role="img" aria-label="Street map showing the academy location"></div>
  </div>
  <div class="divider" style="left:948px"></div>
  <div class="col" style="left:1016px">
    <h4>Follow Us</h4>
    <div class="u" style="width:100px"><i></i></div>
    <ul class="social">
      <li><b></b>Community</li>
      <li><b></b>Updates</li>
      <li><b></b>Reviews</li>
      <li><b></b>Network</li>
    </ul>
  </div>
</footer>

<div class="copyright">Copyright © 2016 Harborline Watch Academy . All Rights Reserved.</div>

</body>
</html>
```